依頼概要
■依頼の目的/概要
カタログギフト向けの高級タオルのラベルデザイン。
(新規提案品)

■ラベルサイズ
縦91mm×横55mm(名刺サイズ)
(添付ファイルをご参照ください。
募集要項・旧ラベル・和紙ラベル(今回提案))

■ラベルに表記したい事項
①商品シリーズ名:鈴音織
(縦書き)
②日本酒のようなワンポイント
(鈴音織という文字に合いそうなハンコ風?ワンポイント)
今回は桜がテーマになります。

■依頼詳細
・商品シリーズ名の由来ですが、日本の四季の自然美の代表的なものとして
・冬の雪
・秋の月
・春の花
の文字をとった『鈴音織』となぞらえた言葉を元に
今回弊社のシリーズ名にしようと企画しました。
第一弾として春の花をテーマに『桜』を題材にしました。
日本人の美へのイメージを伝える商品にしたいと思います。
また海外のお客様にもとっていただけるような商品にしたいと思います。

・贈りものとして、インバウンド需要のお土産として、和風で、美しく
高級感があり、印象に残るデザインを希望します。

■その他
・既に商品提案では期待値の高い弊店の看板商品になる予定です。
今回デザインして頂いたラベルは、長く大切に使わせて頂きたいと
思っております。

・選択させて頂いたデザインの著作権等は弊社に譲渡頂くことが条件になります。

・今後も継続的にお願いする場合も検討しています。

その他何かご不明な点がございましたら、お気軽にご質問下さい。
どうぞよろしくお願いいたします。
■ 選んだ理由

こちらの依頼内容に合致しておりましたので選ばせていだきました。

【ポイント】
・和紙を生かしている
・シンプルかつ高級感ある
・贈り物仕様

■ 提案者全員のお礼・コメント

たくさんの応募いただきありがとうございます。
第2弾としてラベルのコンペ形式をさせていただきました。
今後も企画開発をしていくにあたり様々な形でコンペ形式などで募集をしたいと思いますので
引き続きよろしくお願いいたします。

```html
<!DOCTYPE html>
<html lang="ja">
<head>
<meta charset="utf-8">
<title>鈴音織 ラベル</title>
<link rel="stylesheet" href="https://fonts.googleapis.com/css2?family=Yuji+Boku&family=Quicksand:wght@400&display=swap">
<style>
  :root {
    --washi-light: #fbeef1;
    --washi-mid: #f1cdd6;
    --washi-deep: #e9b7c4;
    --card-white: #ffffff;
    --frame-green: #cfe3a8;
    --name-pink: #d9708b;
    --name-pink-deep: #c2526f;
    --roman-grey: #5a5a5a;
    --stamp-red: #d6262c;
    --petal-pink: #f5c3d0;
  }
  * { margin: 0; padding: 0; box-sizing: border-box; }
  html, body { width: 726px; height: 1200px; overflow: hidden; }
  body { background: #ffffff; }
  .label {
    position: relative;
    width: 726px;
    height: 1200px;
    background:
      radial-gradient(ellipse at 20% 10%, var(--washi-light), transparent 60%),
      radial-gradient(ellipse at 90% 95%, var(--washi-light), transparent 55%),
      linear-gradient(160deg, var(--washi-mid), var(--washi-deep) 50%, var(--washi-mid));
    overflow: hidden;
  }
  .card {
    position: absolute;
    left: 44px; top: 44px;
    width: 638px; height: 1118px;
    background: var(--card-white);
    border: 10px solid var(--frame-green);
    border-radius: 30px;
  }
  .petals {
    position: absolute;
    border-radius: 50%;
    background: radial-gradient(ellipse, rgba(245,195,208,0.55), rgba(245,195,208,0) 70%);
  }
  .petals--upper { left: 60px; top: 60px; width: 320px; height: 380px; }
  .petals--lower { left: 300px; top: 880px; width: 340px; height: 260px; }
  .series-name {
    position: absolute;
    left: 258px; top: 190px;
    writing-mode: vertical-rl;
    font-family: "Yuji Boku", serif;
    font-size: 210px;
    line-height: 1;
    letter-spacing: -4px;
    color: var(--name-pink);
    background: linear-gradient(180deg, var(--name-pink-deep), var(--name-pink) 55%, #eaa0b3);
    -webkit-background-clip: text;
    background-clip: text;
    -webkit-text-fill-color: transparent;
  }
  .series-reading {
    position: absolute;
    left: 486px; top: 168px;
    writing-mode: vertical-rl;
    font-family: "Quicksand", sans-serif;
    font-size: 32px;
    letter-spacing: 2px;
    color: var(--roman-grey);
  }
  .seal {
    position: absolute;
    left: 246px; top: 858px;
    width: 66px; height: 66px;
    background: var(--stamp-red);
    border-radius: 4px;
  }
</style>
</head>
<body>
  <main class="label">
    <section class="card">
      <div class="petals petals--upper" role="img" aria-label="Scattered cherry blossom petals"></div>
      <div class="petals petals--lower" role="img" aria-label="Scattered cherry blossom petals"></div>
      <h1 class="series-name">鈴音織</h1>
      <p class="series-reading">suzu ne ori</p>
      <div class="seal" role="img" aria-label="Red hanko seal with cherry blossom"></div>
    </section>
  </main>
</body>
</html>
```